Business Card

Need a clean, professional, simple, but clever business card for our company LUX RIDES. We only want to see black and white colors as that reflects the branding of our company. Attaching logo. Will also consider the "sky blue" shown in our web site sample png - but use of the color should be minimal.

Lux Rides is a executive car service operating in cities throughout Africa. By operating well equipped Valdren Oster vehicles, we offer the smoothest and stylish ride in town. We aim to provide customers with a valuable experience. That’s why we make sure our patrons get picked up like a boss, travel in style, and arrive fabulous.

We need a card that says that. Likely to print on the best quality/smoothest paper available, as it must speak volumes of our business and class.

We would like the rear of the card to be all black. Perhaps we can put the web url on it, or leave it blank if it looks neater/more elegant.

Use the following contact information (as you see fit):

Lux Rides Limited
P.O. Box 47106
Dar es Salaam, Tanzania

Baraka Kilonzo
Managing Director

+255 (0) 754 829016
sales@luxrides-demo.co.tz

web url: www.luxrides-demo.co.tz
email: chauffeur@luxrides-demo.co.tz

***Winning designer will likely be commissioned for more promotional work in near future.

Target Market(s)

The target market for this card is corporate executives of top firms (financial, consulting, businessmen, etc). They are interested in high quality transportation. Our fleet is all high end Valdren Oster black cars (black exterior, black interior); and therefore, that high end quality and promptness must be reflected in the card. Also simplicity, as we we take care of all the little details behind the scene.

Industry/Entity Type

Business

Requirements
Must have
• Font must be: Helvetica Neue, like the logo. You may use other variations (Thin, Ultra thin, Regular, Bold), so long as it looks and prints well.

If web url is included on the back of the card, then do NOT include it also on the front.
Nice to have
• If there is something nice and clever that you can do/think of that doesn't make the card look busy, but adds a little "posh", then I could be even more interested.

However, if there's no little thing do be done, I'd rather a simple, but very professional looking card that attracts a lot of attention.

```html
<!DOCTYPE html>
<html lang="en">
<head>
<meta charset="utf-8">
<title>Lux Rides — Business Card</title>
<link rel="stylesheet" href="https://fonts.googleapis.com/css2?family=Inter:wght@300;400&family=Open+Sans:wght@400&display=swap">
<style>
  :root {
    --backdrop: #ecebe8;
    --card-white: #ffffff;
    --card-black: #0b0b0b;
    --ink: #1a1a1a;
    --rule: #9a9a9a;
    --paper-text: #ffffff;
    --paper-text-soft: #d8d8d8;
  }
  * { box-sizing: border-box; margin: 0; padding: 0; }
  html, body {
    width: 1200px; height: 900px; overflow: hidden;
    background: var(--backdrop);
  }
  .canvas { position: relative; width: 1200px; height: 900px; }

  .card {
    position: absolute;
    width: 600px; height: 345px;
    box-shadow: 0 10px 28px rgba(0,0,0,.22);
    overflow: hidden;
  }

  /* Front */
  .card-front { left: 70px; top: 80px; background: var(--card-white); }
  .front-wordmark {
    position: absolute; left: 44px; top: 138px;
    font-family: "Inter", sans-serif; font-weight: 300;
    font-size: 36px; letter-spacing: 2px; color: var(--ink);
    white-space: nowrap;
  }
  .front-divider {
    position: absolute; left: 292px; top: 38px;
    width: 1px; height: 200px; background: var(--rule);
  }
  .address {
    position: absolute; left: 312px; top: 40px;
    font-family: "Inter", sans-serif; font-weight: 300;
    font-size: 15px; line-height: 21px; color: var(--ink);
    white-space: nowrap;
  }
  .contact-list {
    position: absolute; left: 312px; top: 150px; list-style: none;
    font-family: "Inter", sans-serif; font-weight: 300;
    font-size: 14px; color: var(--ink);
  }
  .contact-list li { display: flex; align-items: center; height: 24px; white-space: nowrap; }
  .contact-icon { width: 13px; height: 13px; margin-right: 12px; fill: var(--ink); flex: none; }
  .name-band {
    position: absolute; left: 0; bottom: 0;
    width: 100%; height: 100px; background: var(--card-black);
    text-align: center; font-family: "Open Sans", sans-serif;
    color: var(--paper-text);
  }
  .person-name { margin-top: 28px; font-size: 20px; letter-spacing: 1px; }
  .person-title { margin-top: 2px; font-size: 13px; letter-spacing: .5px; color: var(--paper-text-soft); }

  /* Back */
  .card-back { left: 530px; top: 470px; background: var(--card-black); text-align: center; }
  .back-wordmark {
    margin-top: 118px;
    font-family: "Inter", sans-serif; font-weight: 300;
    font-size: 60px; letter-spacing: 5px; color: var(--paper-text);
    white-space: nowrap;
  }
  .back-url {
    margin-top: 22px;
    font-family: "Inter", sans-serif; font-weight: 300;
    font-size: 19px; letter-spacing: .5px; color: var(--paper-text-soft);
  }
</style>
</head>
<body>
<main class="canvas">

  <section class="card card-front" aria-label="Business card front">
    <div class="front-wordmark">LUX RIDES</div>
    <div class="front-divider"></div>
    <p class="address">Lux Rides Limited<br>P.O. Box 47106<br>Dar es Salaam, Tanzania</p>
    <ul class="contact-list">
      <li>
        <svg class="contact-icon" viewBox="0 0 16 16" aria-hidden="true"><path d="M3.5 1 6 3.5 4.6 5.6c.9 2.3 2.8 4.2 5.8 5.8L12.5 10 15 12.5 13 15C7 14 2 9 1 3z"/></svg>
        +255 (0) 754 829016
      </li>
      <li>
        <svg class="contact-icon" viewBox="0 0 16 16" aria-hidden="true"><path d="M1 3h14v10H1zm1.5 1.2 5.5 4.3 5.5-4.3z"/></svg>
        sales@luxrides-demo.co.tz
      </li>
      <li>
        <svg class="contact-icon" viewBox="0 0 16 16" aria-hidden="true"><path d="M1 3h14v10H1zm1.5 1.2 5.5 4.3 5.5-4.3z"/></svg>
        chauffeur@luxrides-demo.co.tz
      </li>
    </ul>
    <div class="name-band">
      <p class="person-name">Baraka Kilonzo</p>
      <p class="person-title">Managing Director</p>
    </div>
  </section>

  <section class="card card-back" aria-label="Business card back">
    <div class="back-wordmark">LUX RIDES</div>
    <p class="back-url">www.luxrides-demo.co.tz</p>
  </section>

</main>
</body>
</html>
```